Bref créative
Boréalis Soins Inc.
Business Cards, Stationnary and enveloppes
Professional
Mathis Lavoie
CFO
512-900 RUE CHAMPFLEURY
Québec, QC ,G2K 3B7
mlavoie@borealissoins-exemple.com
www.borealissoins-exemple.com
Boréalis Soins is a health agency for recruitment of human resources in health (nurse, pharmacist, doctors, etc.) for public and private services.
Boréalis is an emblematic bird of the Province of Québec and is synonym of dexterity, agility, precision, which are important in human care.
Logo + Web site

```html
<!DOCTYPE html>
<html lang="fr">
<head>
<meta charset="utf-8">
<title>Boréalis Soins — papeterie</title>
<link rel="stylesheet" href="https://fonts.googleapis.com/css2?family=Raleway:wght@400;600&display=swap">
<style>
  :root{
    --bg:#ece7e1;
    --paper:#ffffff;
    --red:#b8352a;
    --red-dark:#6f1c14;
    --grey:#6b6b6b;
    --grey-dark:#3a3a3a;
    --ink:#333333;
    --shadow:0 2px 5px rgba(0,0,0,.25);
  }
  *{box-sizing:border-box;margin:0;padding:0}
  html,body{width:1200px;height:310px;overflow:hidden}
  body{background:var(--bg);font-family:"Raleway",sans-serif;color:var(--ink);position:relative}
  .piece{position:absolute;box-shadow:var(--shadow);overflow:hidden}
  .brand{display:flex;align-items:center;gap:5px;font-weight:600;color:var(--grey-dark);letter-spacing:.08em;text-transform:uppercase;white-space:nowrap}
  .brand .mark{display:inline-block;background:var(--red)}
  .paper{background:var(--paper)}
  .red{background:linear-gradient(135deg,var(--red),var(--red-dark))}
  .red .brand{color:#fff}
  .red .brand .mark{background:#fff}
  .faint-mark{position:absolute;background:radial-gradient(circle,rgba(184,53,42,.12),rgba(184,53,42,0) 70%)}

  /* Logo lockup */
  .logo-lockup{position:absolute;left:14px;top:18px}
  .logo-lockup .brand{font-size:34px;gap:12px;color:var(--grey-dark)}
  .logo-lockup .mark{width:26px;height:26px}
  .logo-lockup .tagline{font-size:10px;margin:6px 0 0 40px;color:var(--grey)}

  /* Business cards */
  .card{width:118px;height:70px;padding:8px}
  .card .brand{font-size:8px}
  .card .brand .mark{width:7px;height:7px}
  .card .details{font-size:5px;line-height:1.45;margin-top:10px}
  .red .details{color:#fff}
  .card-a{left:14px;top:168px}
  .card-b{left:138px;top:168px}
  .card-c{left:14px;top:244px}
  .card-d{left:138px;top:244px}

  /* Letterheads */
  .letter{width:160px;height:266px;top:22px;padding:12px}
  .letter .brand{font-size:8px;justify-content:center}
  .letter .brand .mark{width:8px;height:8px}
  .letter .contact{position:absolute;right:12px;top:12px;font-size:4px;line-height:1.5;text-align:right;color:var(--grey)}
  .letter .contact{display:none}
  .letter-a{left:402px}
  .letter-b{left:578px}
  .letter .faint-mark{left:10px;top:40px;width:110px;height:110px}
  .letter-b .band{position:absolute;left:0;right:0;bottom:0;height:28px}
  .letter .foot{position:absolute;left:0;right:0;bottom:9px;text-align:center;font-size:4.5px;color:var(--grey)}
  .letter-b .foot{color:#fff}

  /* Compliment slips */
  .slip{width:156px;height:88px;left:752px;padding:8px}
  .slip .brand{font-size:7px}
  .slip .brand .mark{width:7px;height:7px}
  .slip .faint-mark{left:-10px;top:15px;width:90px;height:90px}
  .slip .band{position:absolute;left:0;right:0;bottom:0;height:14px}
  .slip-a{top:46px}
  .slip-b{top:178px}

  /* Envelopes */
  .envelope{width:250px;height:86px;left:936px}
  .envelope svg{position:absolute;inset:0}
  .envelope .brand{position:absolute;left:10px;top:10px;font-size:7px}
  .envelope .brand .mark{width:7px;height:7px}
  .env-grey{top:46px}
  .env-red{top:114px}
  .env-white{top:196px}
</style>
</head>
<body>

  <div class="logo-lockup">
    <div class="brand"><span class="mark"></span>Boréalis Soins</div>
    <p class="tagline">Recrutement en santé</p>
  </div>

  <div class="piece card paper card-a">
    <div class="brand"><span class="mark"></span>Boréalis Soins</div>
    <div class="details">Mathis Lavoie — CFO<br>512-900 RUE CHAMPFLEURY<br>Québec, QC G2K 3B7<br>mlavoie@borealissoins-exemple.com</div>
  </div>
  <div class="piece card red card-b">
    <div class="brand"><span class="mark"></span>Boréalis Soins</div>
    <div class="details">www.borealissoins-exemple.com<br>Tél. 418 555-0142</div>
  </div>
  <div class="piece card paper card-c">
    <div class="brand"><span class="mark"></span>Boréalis Soins</div>
    <div class="details">Mathis Lavoie — CFO<br>Québec, QC G2K 3B7</div>
  </div>
  <div class="piece card red card-d">
    <div class="brand"><span class="mark"></span>Boréalis Soins</div>
    <div class="details">www.borealissoins-exemple.com<br>Tél. 418 555-0142</div>
  </div>

  <div class="piece letter paper letter-a">
    <div class="brand"><span class="mark"></span>Boréalis Soins</div>
    <div class="faint-mark" role="img" aria-label="Emblème de la marque en filigrane"></div>
    <div class="foot">512-900 RUE CHAMPFLEURY, Québec, QC G2K 3B7 · www.borealissoins-exemple.com</div>
  </div>
  <div class="piece letter paper letter-b">
    <div class="brand"><span class="mark"></span>Boréalis Soins</div>
    <div class="faint-mark" role="img" aria-label="Emblème de la marque en filigrane"></div>
    <div class="band red"></div>
    <div class="foot">512-900 RUE CHAMPFLEURY, Québec, QC G2K 3B7 · Tél. 418 555-0142</div>
  </div>

  <div class="piece slip paper slip-a">
    <div class="brand"><span class="mark"></span>Boréalis Soins</div>
    <div class="faint-mark" role="img" aria-label="Emblème de la marque en filigrane"></div>
  </div>
  <div class="piece slip paper slip-b">
    <div class="brand"><span class="mark"></span>Boréalis Soins</div>
    <div class="faint-mark" role="img" aria-label="Emblème de la marque en filigrane"></div>
    <div class="band red"></div>
  </div>

  <div class="piece envelope env-grey paper">
    <svg width="250" height="86" viewBox="0 0 250 86" aria-hidden="true">
      <defs><linearGradient id="flapGrey" x1="0" y1="0" x2="0" y2="1"><stop offset="0" stop-color="#8a8a8a"/><stop offset="1" stop-color="#3a3a3a"/></linearGradient></defs>
      <polygon points="0,0 250,0 125,44" fill="url(#flapGrey)"/>
    </svg>
  </div>
  <div class="piece envelope env-red paper">
    <svg width="250" height="86" viewBox="0 0 250 86" aria-hidden="true">
      <defs><linearGradient id="flapRed" x1="0" y1="0" x2="0" y2="1"><stop offset="0" stop-color="#b8352a"/><stop offset="1" stop-color="#6f1c14"/></linearGradient></defs>
      <polygon points="0,0 250,0 125,44" fill="url(#flapRed)"/>
    </svg>
  </div>
  <div class="piece envelope env-white paper">
    <svg width="250" height="86" viewBox="0 0 250 86" aria-hidden="true">
      <polyline points="0,0 125,44 250,0" fill="none" stroke="#d8d8d8" stroke-width="1"/>
    </svg>
    <div class="brand"><span class="mark"></span>Boréalis Soins</div>
  </div>

</body>
</html>
```